Simple and Clean business card design

We would like the design to be simple clean and to incorporate our colors.

We are open to your design and talent, we have the dots in our logo as we think of it as data points and we connect data points for people.

We are open to see the great creative and clean design you bring to the table

Contact Information for Business Card

please include: name, position, email, phone and website

Font styles to use
Sans Serif

Requirements
Must have
• my colors incorporated, simplicity
Nice to have
• lots of white space, simplicity
Should not have
• complexicity/ complex art

```html
<!DOCTYPE html>
<html lang="en">
<head>
<meta charset="utf-8">
<title>Meadowlink Business Card</title>
<link rel="stylesheet" href="https://fonts.googleapis.com/css2?family=Montserrat:wght@400;500&display=swap">
<style>
  :root {
    --page-bg: #2a2a2c;
    --card-bg: #1c1c1e;
    --ink: #ffffff;
    --ink-soft: #e6e6e6;
    --accent-yellow: #f5b800;
    --accent-blue: #5b7fc8;
    --accent-green: #2faa4a;
    --accent-red: #e0392b;
  }
  * { box-sizing: border-box; margin: 0; padding: 0; }
  html, body { width: 1200px; height: 909px; overflow: hidden; }
  body {
    background: var(--page-bg);
    font-family: "Montserrat", sans-serif;
    display: flex;
    align-items: center;
    justify-content: center;
    gap: 40px;
  }
  .card {
    position: relative;
    width: 560px;
    height: 320px;
    background: var(--card-bg);
    overflow: hidden;
    box-shadow: 0 12px 30px rgba(0,0,0,.45);
  }
  .colour-band {
    position: absolute;
    left: 0; right: 0; bottom: 0;
    height: 6px;
    display: flex;
  }
  .colour-band span { flex: 1; }
  .colour-band .band-blue { background: var(--accent-blue); }
  .colour-band .band-green { background: var(--accent-green); }
  .colour-band .band-yellow { background: var(--accent-yellow); }
  .colour-band .band-red { background: var(--accent-red); }

  .wordmark {
    position: absolute;
    display: flex;
    align-items: center;
    gap: 10px;
    color: var(--ink);
    font-weight: 500;
    letter-spacing: 0.5px;
    line-height: 1;
  }
  .wordmark-dot {
    width: 12px; height: 12px;
    border-radius: 50%;
    background: var(--accent-blue);
  }
  .card-front .wordmark { left: 44px; top: 40px; font-size: 48px; }
  .card-back .wordmark { left: 50%; top: 50%; transform: translate(-50%, -50%); font-size: 44px; }

  .identity { position: absolute; left: 44px; top: 124px; }
  .person-name { font-size: 19px; font-weight: 500; color: var(--ink); letter-spacing: 0.5px; }
  .person-name .given { color: var(--accent-yellow); }
  .person-role { font-size: 15px; color: var(--ink-soft); margin-top: 2px; }

  .contacts { position: absolute; left: 44px; top: 196px; list-style: none; }
  .contacts li {
    display: flex; align-items: center; gap: 9px;
    font-size: 13px; color: var(--ink-soft); line-height: 22px;
  }
  .contacts svg { width: 11px; height: 11px; fill: var(--accent-yellow); flex: none; }

  .address {
    position: absolute; left: 300px; top: 240px;
    padding-left: 20px;
    border-left: 1.5px solid var(--ink-soft);
    font-size: 13px; color: var(--ink-soft); line-height: 20px;
    font-style: normal;
  }
</style>
</head>
<body>

<section class="card card-front" aria-label="Business card front">
  <div class="wordmark"><span>Meadowlink</span><span class="wordmark-dot"></span></div>

  <div class="identity">
    <p class="person-name"><span class="given">ROWAN</span> HALE</p>
    <p class="person-role">Founder/ CEO</p>
  </div>

  <ul class="contacts">
    <li>
      <svg viewBox="0 0 24 24"><path d="M6.6 10.8a15.1 15.1 0 0 0 6.6 6.6l2.2-2.2a1 1 0 0 1 1-.25 11.4 11.4 0 0 0 3.6.57 1 1 0 0 1 1 1V20a1 1 0 0 1-1 1A17 17 0 0 1 3 4a1 1 0 0 1 1-1h3.5a1 1 0 0 1 1 1c0 1.25.2 2.45.57 3.57a1 1 0 0 1-.25 1z"/></svg>
      555-014-2290
    </li>
    <li>
      <svg viewBox="0 0 24 24"><path d="M2 5h20v14H2zm2 2v.5l8 5 8-5V7l-8 5z"/></svg>
      rowan.hale@meadowlink.io
    </li>
    <li>
      <svg viewBox="0 0 24 24"><circle cx="12" cy="12" r="10"/></svg>
      www.Meadowlink.io
    </li>
  </ul>

  <address class="address">18 Ledger Lane<br>Fairbrook, IL 60000</address>

  <div class="colour-band" aria-hidden="true">
    <span class="band-blue"></span><span class="band-green"></span><span class="band-yellow"></span><span class="band-red"></span>
  </div>
</section>

<section class="card card-back" aria-label="Business card back">
  <div class="wordmark"><span>Meadowlink</span><span class="wordmark-dot"></span></div>

  <div class="colour-band" aria-hidden="true">
    <span class="band-blue"></span><span class="band-green"></span><span class="band-yellow"></span><span class="band-red"></span>
  </div>
</section>

</body>
</html>
```